Emergency Vehicle Installer and Security Firm Needs a Business Card

Our company "Corvalt" need a business card for our Emergency Vehicle Equipment Installation and Infrastructure Security Business. We are contract designers, manufacturers and installers for Emergency Vehicle Fleets. This includes installation of Emergency Lights, Sirens, Vehicle Graphics and Radio Communications. We also supply this products to an international market. We also do consultant, and installation of high level security access, alarm and surveillance equipment for medium to large size businesses.

The design should represent a level of trust in our professionalism and expertise. It should visually display our ongoing relationship with the emergency services, but not overtake our commitment to high level security options.

Target Market(s)

Emergency Services and Businesses requiring high level security

Industry/Entity Type

Business

Contact Information for Business Card

*note complete details will be given to the winning designer for revising. The name "Mark Pell will be used to fill in name".

Mark Pell
Managing Director
Corvalt NZ Limited
Phone: +64 027 604 91352
Email: mark.pell@corvalt-example.co.nz

Requirements
Must have
• Card must be in black. Using our logo on the top as supplied. Designers should try having the reverse side as a blurred image of police lights (red and blue) with our logo in greyscale in the centre (this is not particularly a requirement, but feel free to play around with this option).
Nice to have
• A card design that looks good when spot UV printed. A clean compact and graphic design. A grey scale feel on the front (excluding logo, but you can play around with that idea). Rounded smooth text.
Should not have
• Will update this section as designs come through - feel free to submit what you feel would look good.

```html
<!DOCTYPE html>
<html lang="en">
<head>
<meta charset="utf-8">
<title>Corvalt Business Card</title>
<link href="https://fonts.googleapis.com/css2?family=Roboto:wght@300;400;700;900&display=swap" rel="stylesheet">
<style>
  :root {
    --page: #ffffff;
    --card: #1c1c1c;
    --red: #e41e26;
    --white: #ffffff;
    --muted: #d6d6d6;
    --shadow: rgba(0, 0, 0, 0.28);
  }
  html, body {
    margin: 0;
    padding: 0;
    width: 1200px;
    height: 1200px;
    overflow: hidden;
    background: var(--page);
    font-family: "Roboto", Arial, sans-serif;
  }
  .canvas {
    position: relative;
    width: 1200px;
    height: 1200px;
  }
  .card {
    position: absolute;
    background: var(--card);
    box-shadow: 0 8px 18px var(--shadow);
    overflow: hidden;
  }
  .card--front {
    left: 322px;
    top: 112px;
    width: 592px;
    height: 338px;
  }
  .card--back {
    left: 434px;
    top: 527px;
    width: 338px;
    height: 591px;
  }
  .brand-rule {
    position: absolute;
    top: 165px;
    height: 3px;
    background: var(--red);
  }
  .brand-rule--left { left: 0; width: 134px; }
  .brand-rule--right { right: 0; width: 134px; }
  .wordmark {
    position: absolute;
    left: 0;
    right: 0;
    text-align: center;
    font-weight: 900;
    color: var(--white);
    letter-spacing: 1px;
    line-height: 1;
  }
  .card--front .wordmark {
    top: 132px;
    font-size: 62px;
  }
  .card--back .wordmark {
    top: 114px;
    font-size: 54px;
  }
  .person {
    position: absolute;
    left: 65px;
    top: 372px;
  }
  .person__name {
    margin: 0;
    font-size: 31px;
    font-weight: 300;
    color: var(--red);
    line-height: 1;
    letter-spacing: 0.5px;
  }
  .person__name strong { font-weight: 700; }
  .person__title {
    margin: 5px 0 0 3px;
    font-size: 14px;
    font-weight: 300;
    color: var(--muted);
    letter-spacing: 0.3px;
  }
  .contact {
    position: absolute;
    left: 46px;
    top: 449px;
    margin: 0;
    padding: 0;
    list-style: none;
  }
  .contact__company {
    padding-left: 19px;
    font-size: 15px;
    font-weight: 700;
    color: var(--white);
    margin-bottom: 6px;
  }
  .contact__item {
    display: flex;
    align-items: center;
    height: 23px;
    font-size: 14px;
    font-weight: 300;
    color: var(--muted);
  }
  .contact__icon {
    width: 16px;
    height: 14px;
    margin-right: 11px;
    flex: none;
  }
</style>
</head>
<body>
<main class="canvas">
  <section class="card card--front" aria-label="Card front">
    <div class="brand-rule brand-rule--left"></div>
    <div class="brand-rule brand-rule--right"></div>
    <div class="wordmark">CORVALT</div>
  </section>

  <section class="card card--back" aria-label="Card back">
    <div class="wordmark">CORVALT</div>
    <div class="person">
      <h1 class="person__name">MARK <strong>PELL</strong></h1>
      <p class="person__title">MANAGING DIRECTOR</p>
    </div>
    <ul class="contact">
      <li class="contact__company">CORVALT NZ LIMITED</li>
      <li class="contact__item">
        <svg class="contact__icon" viewBox="0 0 16 16" aria-hidden="true">
          <path fill="#e41e26" d="M3.2 1.2l2.4 2.9-1.3 1.6c.9 2 2.3 3.4 4.2 4.3l1.6-1.3 2.9 2.3-1.4 2.6C6.6 13.6 2.3 9.3 1 4.2z"/>
        </svg>
        +64 027 604 91352
      </li>
      <li class="contact__item">
        <svg class="contact__icon" viewBox="0 0 16 12" aria-hidden="true">
          <rect x="0" y="0" width="16" height="12" fill="#e41e26"/>
          <path d="M0.5 0.8L8 6.8l7.5-6M0.5 11.3l5.5-5M15.5 11.3l-5.5-5" fill="none" stroke="#1c1c1c" stroke-width="1.2"/>
        </svg>
        MARK.PELL@CORVALT-EXAMPLE.CO.NZ
      </li>
    </ul>
  </section>
</main>
</body>
</html>
```